Powepoint template for an investment group

Need high end clear clean concise creative luxurious

Have royal clients
High end/billionaire investors

Using ross gold logo can be creative
Must habe page numbers
Logo preference header top right
Page number footer bottom right

The first page of the ppt maybe a big block of dark grey and oberi investment group written on the front page in rose gold

Target Market(s)

Investors at a high level

Requirements
Must have
• Luxury feel

```html
<!DOCTYPE html>
<html lang="en">
<head>
<meta charset="utf-8">
<title>Oberi Investment Group – Presentation Template</title>
<link rel="stylesheet" href="https://fonts.googleapis.com/css2?family=Roboto:wght@300;400;500;700&display=swap">
<style>
  :root {
    --page-bg: #fbeeed;
    --rose: #c4837a;
    --rose-deep: #b06c62;
    --rose-soft: #e4a99c;
    --charcoal: #2a2a2b;
    --ink: #2b2b2b;
    --body: #6a6a6a;
    --white: #ffffff;
  }
  * { box-sizing: border-box; margin: 0; padding: 0; }
  html, body { width: 803px; height: 1200px; overflow: hidden; }
  body { background: var(--page-bg); font-family: "Roboto", sans-serif; position: relative; }

  .slide { position: absolute; width: 320px; height: 240px; overflow: hidden; background: var(--white); box-shadow: 0 2px 6px rgba(150, 90, 80, .08); }
  .col-left { left: 61px; }
  .col-right { left: 423px; }
  .row-1 { top: 61px; } .row-2 { top: 341px; } .row-3 { top: 620px; } .row-4 { top: 899px; }

  .photo { position: absolute; }
  .page-tab { position: absolute; right: 0; bottom: 0; width: 66px; height: 15px; background: var(--rose); clip-path: polygon(10px 0, 100% 0, 100% 100%, 0 100%); color: var(--white); font-size: 6px; font-weight: 700; display: flex; align-items: center; justify-content: flex-end; padding-right: 21px; }
  .page-tab.plain { background: transparent; }

  /* Brand name, set as plain text */
  .brand-name { position: absolute; top: 12px; right: 22px; display: flex; align-items: center; font-size: 5.6px; font-weight: 500; line-height: 1; white-space: nowrap; }
  .brand-name .dot { width: 5px; height: 5px; border-radius: 50%; background: currentColor; margin-right: 3px; }
  .brand-name.on-rose { color: var(--white); }
  .brand-name.on-white { color: var(--rose); }

  .heading { font-weight: 700; letter-spacing: .8px; line-height: 1; }

  /* Slide 1 */
  .cover { background: var(--charcoal); }
  .cover .photo { inset: 0; background: radial-gradient(ellipse at 50% 45%, #3a3a3b 0%, #2a2a2b 60%, #222223 100%); }
  .cover-name { position: absolute; left: 0; right: 0; top: 100px; display: flex; align-items: center; justify-content: center; font-size: 24px; font-weight: 300; color: var(--rose-soft); line-height: 1; }
  .cover-name .dot { width: 12px; height: 12px; border-radius: 50%; background: var(--rose-soft); margin-right: 10px; }

  /* Slide 2 */
  .agenda .photo { inset: 0; background: linear-gradient(135deg, #8e4f45 0%, #c98d7f 45%, #e6c4b6 70%, #a9685c 100%); }
  .agenda .cut { position: absolute; inset: 0; }
  .agenda .heading { position: absolute; left: 216px; top: 77px; font-size: 17px; color: var(--ink); }
  .agenda-list { position: absolute; left: 203px; top: 101px; list-style: none; }
  .agenda-list li { display: flex; align-items: center; height: 15.7px; font-size: 4.8px; color: #444; }
  .agenda-list .dot { width: 7px; height: 7px; border-radius: 50%; background: var(--rose); margin-right: 8px; display: flex; align-items: center; justify-content: center; }

  /* Rose slides */
  .rose-slide { background: var(--rose); }
  .rose-slide .photo { inset: 0; background: linear-gradient(160deg, #d3a197 0%, #c68a80 50%, #bd7d73 100%); }
  .what .heading { position: absolute; left: 0; right: 0; top: 26px; text-align: center; font-size: 16px; color: var(--white); }
  .what-list { position: absolute; top: 54px; left: 0; right: 0; list-style: none; }
  .what-list li { position: absolute; display: flex; align-items: center; font-size: 4.6px; color: var(--white); white-space: nowrap; }
  .what-list .arrow { width: 9px; margin-right: 7px; }
  .what .team-photo { position: absolute; left: 0; bottom: 0; width: 320px; height: 92px; }

  .mission .heading { position: absolute; left: 0; right: 0; top: 78px; text-align: center; font-size: 18px; color: var(--white); }
  .mission p { position: absolute; left: 40px; right: 40px; top: 113px; text-align: center; font-size: 7px; line-height: 12.4px; color: #fdf1ef; font-weight: 400; }

  /* Slide 5 */
  .who .panel { position: absolute; left: 0; top: 0; width: 160px; height: 240px; background: var(--rose); }
  .who .heading { position: absolute; left: 30px; top: 38px; font-size: 17px; color: var(--white); line-height: 1.25; }
  .framed { position: absolute; border: 2px solid var(--white); box-shadow: 0 2px 6px rgba(0,0,0,.18); }
  .who .photo-top { left: 144px; top: 20px; width: 145px; height: 87px; background: linear-gradient(135deg, #2c2c2e, #6f5f5a 55%, #b83a3a); }
  .who .photo-bottom { left: 29px; top: 99px; width: 145px; height: 120px; background: linear-gradient(135deg, #9aa1a8, #d6a35a 45%, #b9c9dc); }
  .who p { position: absolute; left: 187px; top: 128px; width: 106px; font-size: 5.3px; line-height: 9.2px; color: var(--body); }

  /* Slide 6 */
  .investors .photo { inset: 0; background: linear-gradient(135deg, #8e4f45 0%, #c98d7f 45%, #e6c4b6 70%, #a9685c 100%); }
  .investors .heading { position: absolute; left: 29px; top: 46px; font-size: 17px; color: var(--ink); }
  .investors p { position: absolute; left: 30px; top: 74px; width: 112px; font-size: 5.6px; line-height: 9.2px; color: var(--body); }
  .partner { position: absolute; display: flex; align-items: center; font-size: 11px; font-weight: 500; color: #3a3a3a; }
  .partner .mark { width: 8px; height: 8px; border-radius: 50%; background: var(--rose); margin-right: 4px; }

  /* Slide 7 */
  .strategy .heading { position: absolute; left: 0; right: 0; top: 29px; text-align: center; font-size: 17px; color: var(--ink); }
  .step-label { position: absolute; width: 60px; text-align: center; font-size: 6.4px; color: #555; }
  .step-note { position: absolute; width: 66px; text-align: center; }
  .step-note h3 { font-size: 6.2px; font-weight: 500; color: #555; margin-bottom: 4px; }
  .step-note p { font-size: 4.2px; line-height: 7px; color: var(--body); }
  .strategy svg.track { position: absolute; inset: 0; }

  /* Slide 8 */
  .contact { background: var(--charcoal); }
  .contact .photo { inset: 0; background: radial-gradient(ellipse at 50% 30%, #333334 0%, #2a2a2b 60%, #252526 100%); }
  .contact .heading { position: absolute; left: 0; right: 0; top: 68px; text-align: center; font-size: 17px; color: var(--white); }
  .contact-row { position: absolute; display: flex; align-items: center; color: var(--white); font-size: 7.6px; }
  .contact-row svg { margin-right: 8px; }
  .contact-row.address { font-size: 5.6px; }
  .copyright { position: absolute; left: 0; right: 0; top: 222px; text-align: center; font-size: 4px; color: #ddd; }
</style>
</head>
<body>

<!-- Cover -->
<section class="slide cover col-left row-1">
  <div class="photo" role="img" aria-label="Dimly lit office meeting room behind a dark overlay"></div>
  <div class="cover-name"><span class="dot"></span>Oberi Investment Group</div>
  <div class="page-tab plain">Page 1/8</div>
</section>

<!-- Agenda -->
<section class="slide agenda col-right row-1">
  <div class="photo" role="img" aria-label="Overhead view of a team reviewing charts at a desk, rose-tinted"></div>
  <svg class="cut" width="320" height="240" viewBox="0 0 320 240"><polygon points="211,0 320,0 320,240 138,240" fill="#fff"/></svg>
  <div class="brand-name on-white" style="top:24px;right:28px;font-size:7px"><span class="dot" style="width:6px;height:6px"></span>Oberi Investment Group</div>
  <h2 class="heading">AGENDA</h2>
  <ul class="agenda-list">
    <li><span class="dot"><svg width="5" height="4" viewBox="0 0 5 4"><path d="M0 2h4M2.6.7 4 2 2.6 3.3" stroke="#fff" stroke-width=".8" fill="none"/></svg></span>Lorem Ipsum dolor dummy text</li>
    <li><span class="dot"><svg width="5" height="4" viewBox="0 0 5 4"><path d="M0 2h4M2.6.7 4 2 2.6 3.3" stroke="#fff" stroke-width=".8" fill="none"/></svg></span>Lorem dolor dummy text</li>
    <li><span class="dot"><svg width="5" height="4" viewBox="0 0 5 4"><path d="M0 2h4M2.6.7 4 2 2.6 3.3" stroke="#fff" stroke-width=".8" fill="none"/></svg></span>Lorem Ipsum dolor</li>
    <li><span class="dot"><svg width="5" height="4" viewBox="0 0 5 4"><path d="M0 2h4M2.6.7 4 2 2.6 3.3" stroke="#fff" stroke-width=".8" fill="none"/></svg></span>Lorem Ipsum dolor dummy text</li>
    <li><span class="dot"><svg width="5" height="4" viewBox="0 0 5 4"><path d="M0 2h4M2.6.7 4 2 2.6 3.3" stroke="#fff" stroke-width=".8" fill="none"/></svg></span>Lorem Ipsum</li>
    <li><span class="dot"><svg width="5" height="4" viewBox="0 0 5 4"><path d="M0 2h4M2.6.7 4 2 2.6 3.3" stroke="#fff" stroke-width=".8" fill="none"/></svg></span>Lorem Ipsum dolor</li>
  </ul>
  <div class="page-tab">Page 2/6</div>
</section>

<!-- What we do -->
<section class="slide rose-slide what col-left row-2">
  <div class="photo" role="img" aria-label="Office meeting scene under a rose overlay"></div>
  <div class="brand-name on-rose"><span class="dot"></span>Oberi Investment Group</div>
  <h2 class="heading">WHAT WE DO</h2>
  <ul class="what-list">
    <li style="left:65px;top:0"><svg class="arrow" width="9" height="4" viewBox="0 0 9 4"><path d="M0 2h8.4M6.6.4 8.4 2 6.6 3.6" stroke="#fff" stroke-width=".5" fill="none"/></svg>Lorem Ipsum is simply dummy text of the printing and typesetting industry.</li>
    <li style="left:100px;top:17px"><svg class="arrow" width="9" height="4" viewBox="0 0 9 4"><path d="M0 2h8.4M6.6.4 8.4 2 6.6 3.6" stroke="#fff" stroke-width=".5" fill="none"/></svg>Lorem Ipsum is simply dummy text industry.</li>
    <li style="left:82px;top:34px"><svg class="arrow" width="9" height="4" viewBox="0 0 9 4"><path d="M0 2h8.4M6.6.4 8.4 2 6.6 3.6" stroke="#fff" stroke-width=".5" fill="none"/></svg>Lorem Ipsum is simply dummy text and typesetting industry.</li>
    <li style="left:94px;top:51px"><svg class="arrow" width="9" height="4" viewBox="0 0 9 4"><path d="M0 2h8.4M6.6.4 8.4 2 6.6 3.6" stroke="#fff" stroke-width=".5" fill="none"/></svg>Lorem Ipsum is simply dummy text of the printing</li>
    <li style="left:111px;top:68px"><svg class="arrow" width="9" height="4" viewBox="0 0 9 4"><path d="M0 2h8.4M6.6.4 8.4 2 6.6 3.6" stroke="#fff" stroke-width=".5" fill="none"/></svg>Lorem Ipsum is simply dummy text</li>
  </ul>
  <svg class="team-photo" width="320" height="92" viewBox="0 0 320 92" role="img" aria-label="Silhouetted team seated around a boardroom table against bright windows">
    <defs>
      <linearGradient id="teamTone" x1="0" y1="0" x2="1" y2="0">
        <stop offset="0" stop-color="#2c3a5a"/><stop offset=".5" stop-color="#c9b7b8"/><stop offset="1" stop-color="#2a3656"/>
      </linearGradient>
      <linearGradient id="teamShade" x1="0" y1="0" x2="0" y2="1">
        <stop offset="0" stop-color="#000" stop-opacity="0"/><stop offset="1" stop-color="#1a1a22" stop-opacity=".65"/>
      </linearGradient>
    </defs>
    <path d="M0 36 Q160 -10 320 36 V92 H0Z" fill="url(#teamTone)"/>
    <path d="M0 36 Q160 -10 320 36 V92 H0Z" fill="url(#teamShade)"/>
  </svg>
  <div class="page-tab">Page 3/8</div>
</section>

<!-- Mission -->
<section class="slide rose-slide mission col-right row-2">
  <div class="photo" role="img" aria-label="Presenter addressing a seated audience under a rose overlay"></div>
  <div class="brand-name on-rose"><span class="dot"></span>Oberi Investment Group</div>
  <h2 class="heading">OUR MISSION</h2>
  <p>Lorem ipsum dolor sit amet, consectetur adipiscing elit, sed do eiusmod tempor incididunt ut labore et dolore magna aliqua. Quis ipsum suspendisse ultrices gravida. Risus commodo viverra maecenas accumsan lacus vel facilisis.</p>
  <div class="page-tab plain">Page 4/8</div>
</section>

<!-- Who we are -->
<section class="slide who col-left row-3">
  <div class="panel"></div>
  <h2 class="heading">WHO<br>WE ARE</h2>
  <div class="framed photo-top" role="img" aria-label="Businesswoman seated on a sofa writing in a red notebook"></div>
  <div class="framed photo-bottom" role="img" aria-label="Two colleagues working together at a laptop in an office"></div>
  <p>Lorem ipsum dolor sit amet, consectetur adipiscing elit, sed do eiusmod tempor incididunt ut labore et dolore magna aliqua. Quis ipsum suspendisse ultrices gravida. Risus commodo viverra maecenas accumsan lacus vel facilisis. Lorem ipsum dolor sit amet, consectetur adipiscing elit, sed do eiusmod tempor incididunt ut labore et dolore magna</p>
  <div class="page-tab">Page 5/8</div>
</section>

<!-- Investors -->
<section class="slide investors col-right row-3">
  <div class="photo" role="img" aria-label="Overhead view of a team reviewing charts at a desk, rose-tinted"></div>
  <svg style="position:absolute;inset:0" width="320" height="240" viewBox="0 0 320 240"><polygon points="0,0 140,0 213,240 0,240" fill="#fff"/></svg>
  <div class="brand-name on-rose"><span class="dot"></span>Oberi Investment Group</div>
  <h2 class="heading">INVESTORS</h2>
  <p>Lorem ipsum dolor sit amet, consectetur adipiscing elit, sed do eiusmod tempor incididunt ut labore et dolore magna aliqua. Quis ipsum</p>
  <div class="partner" style="left:30px;top:124px"><span class="mark"></span>orbit</div>
  <div class="partner" style="left:95px;top:124px"><span class="mark"></span>lumen</div>
  <div class="partner" style="left:30px;top:150px"><span class="mark"></span>velo.</div>
  <div class="partner" style="left:95px;top:150px"><span class="mark"></span>nora.</div>
  <div class="partner" style="left:30px;top:176px"><span class="mark"></span>cubix</div>
  <div class="partner" style="left:95px;top:176px"><span class="mark"></span>markly</div>
  <div class="page-tab">Page 6/8</div>
</section>

<!-- Strategy -->
<section class="slide strategy col-left row-4">
  <svg style="position:absolute;left:0;top:0" width="29" height="50" viewBox="0 0 29 50"><polygon points="0,0 29,0 0,50" fill="var(--rose)"/></svg>
  <div class="brand-name on-white"><span class="dot"></span>Oberi Investment Group</div>
  <h2 class="heading">OUR STRATEGY</h2>
  <svg class="track" width="320" height="240" viewBox="0 0 320 240">
    <defs>
      <linearGradient id="disc" x1="0" y1="0" x2="0" y2="1"><stop offset="0" stop-color="#fafafa"/><stop offset="1" stop-color="#dcdcdc"/></linearGradient>
    </defs>
    <path d="M53 131 L122 157 L196 131 L268 157" stroke="#bdbdbd" stroke-width="3" fill="none"/>
    <g>
      <ellipse cx="53" cy="134" rx="25" ry="11" fill="url(#disc)"/><ellipse cx="53" cy="131" rx="19" ry="8" fill="#fff" stroke="#e3e3e3"/>
      <circle cx="53" cy="124" r="9" fill="var(--rose)" stroke="#f3d6d0" stroke-width="2"/>
      <path d="M49 121h4v3h-4zM54 125h3v3h-3zM51 124v3h3" stroke="#fff" stroke-width=".8" fill="none"/>
    </g>
    <g>
      <ellipse cx="122" cy="160" rx="25" ry="11" fill="url(#disc)"/><ellipse cx="122" cy="157" rx="19" ry="8" fill="#fff" stroke="#e3e3e3"/>
      <circle cx="122" cy="150" r="9" fill="#f3d6d0"/>
      <path d="M118 154v-7M118 154h8M120 152v-3M122 152v-4M124 152v-2" stroke="var(--rose-deep)" stroke-width="1" fill="none"/>
    </g>
    <g>
      <ellipse cx="196" cy="134" rx="25" ry="11" fill="url(#disc)"/><ellipse cx="196" cy="131" rx="19" ry="8" fill="#fff" stroke="#e3e3e3"/>
      <circle cx="196" cy="124" r="9" fill="var(--rose)" stroke="#f3d6d0" stroke-width="2"/>
      <circle cx="196" cy="124" r="4" stroke="#fff" stroke-width=".8" fill="none"/><circle cx="196" cy="124" r="1.5" fill="#fff"/>
    </g>
    <g>
      <ellipse cx="268" cy="160" rx="25" ry="11" fill="url(#disc)"/><ellipse cx="268" cy="157" rx="19" ry="8" fill="#fff" stroke="#e3e3e3"/>
      <circle cx="268" cy="150" r="9" fill="#f3d6d0"/>
      <path d="M265 146h6v3h-6zM268 149v5M265 154h6" stroke="var(--rose-deep)" stroke-width="1" fill="none"/>
    </g>
  </svg>
  <div class="step-label" style="left:23px;top:103px">Step 1</div>
  <div class="step-label" style="left:92px;top:129px">Step 2</div>
  <div class="step-label" style="left:166px;top:103px">Step 3</div>
  <div class="step-label" style="left:238px;top:129px">Step 4</div>
  <div class="step-note" style="left:89px;top:85px"><h3>Heading Goes Here</h3><p>Lorem ipsum dolor sit amet, consectetur adipiscing elit, sed do eiusmod</p></div>
  <div class="step-note" style="left:235px;top:85px"><h3>Heading Goes Here</h3><p>Lorem ipsum dolor sit amet, consectetur adipiscing elit, sed do eiusmod</p></div>
  <div class="step-note" style="left:20px;top:179px"><h3>Heading Goes Here</h3><p>Lorem ipsum dolor sit amet, consectetur adipiscing elit, sed do eiusmod</p></div>
  <div class="step-note" style="left:163px;top:179px"><h3>Heading Goes Here</h3><p>Lorem ipsum dolor sit amet, consectetur adipiscing elit, sed do eiusmod</p></div>
  <div class="page-tab">Page 7/8</div>
</section>

<!-- Contact -->
<section class="slide contact col-right row-4">
  <div class="photo" role="img" aria-label="Business team in an office behind a dark overlay"></div>
  <h2 class="heading">CONTACT INFORMATION</h2>
  <div class="contact-row" style="left:120px;top:110px">
    <svg width="11" height="8" viewBox="0 0 11 8"><rect width="11" height="8" rx="1" fill="var(--rose)"/><path d="M.5 .8 5.5 4.6 10.5 .8" stroke="#2a2a2b" stroke-width=".9" fill="none"/></svg><span>hello@oberigroup.com</span>
  </div>
  <div class="contact-row" style="left:120px;top:134px">
    <svg width="11" height="11" viewBox="0 0 24 24"><path d="M6.6 10.8a15 15 0 0 0 6.6 6.6l2.2-2.2a1 1 0 0 1 1-.25 11.4 11.4 0 0 0 3.6.57 1 1 0 0 1 1 1V20a1 1 0 0 1-1 1A17 17 0 0 1 3 4a1 1 0 0 1 1-1h3.5a1 1 0 0 1 1 1c0 1.25.2 2.45.57 3.57a1 1 0 0 1-.25 1Z" fill="var(--rose)"/></svg><span>+1 555 010-2468</span>
  </div>
  <div class="contact-row address" style="left:94px;top:156px">
    <svg width="10" height="14" viewBox="0 0 10 14"><path d="M5 0a5 5 0 0 0-5 5c0 3.8 5 9 5 9s5-5.2 5-9a5 5 0 0 0-5-5Z" fill="var(--rose)"/><circle cx="5" cy="5" r="1.8" fill="#2a2a2b"/></svg><span>48 Harbor Lane, Sample City 102 300</span>
  </div>
  <div class="copyright">Copyright © 2022 Oberi Group | All Rights Reserved.</div>
</section>

</body>
</html>
```